Business Card Design

Massage therapy and healthy food
Zenova Health Massage (business name)

Target Market(s)

Health conscious

Industry/Entity Type

Business

Contact Information for Business Card

0413886207

Font styles to use
Serif

```html
<!DOCTYPE html>
<html lang="en">
<head>
<meta charset="utf-8">
<title>Zenova Health Massage – Business Card</title>
<link href="https://fonts.googleapis.com/css2?family=Questrial&family=Tinos:wght@400;700&display=swap" rel="stylesheet">
<style>
  :root {
    --backdrop: #e6e8e6;
    --leaf-green: #8cc63f;
    --leaf-green-light: #a6d467;
    --ink: #111111;
    --card-white: #ffffff;
    --wave-blue: #0d9fc0;
    --wave-blue-deep: #0a86a6;
    --wave-line: #b5d56a;
  }
  * { margin: 0; padding: 0; box-sizing: border-box; }
  html, body {
    width: 1200px;
    height: 871px;
    overflow: hidden;
    background: var(--backdrop);
  }
  .canvas {
    position: relative;
    width: 1200px;
    height: 871px;
  }
  .card {
    position: absolute;
    width: 620px;
    height: 354px;
    border-radius: 4px;
    overflow: hidden;
    box-shadow: 0 10px 28px rgba(0,0,0,0.22);
  }
  /* Front: green logo side */
  .card--front {
    left: 70px;
    top: 50px;
    background: linear-gradient(135deg, var(--leaf-green-light), var(--leaf-green) 55%);
  }
  .brand {
    position: absolute;
    display: flex;
    align-items: center;
    gap: 14px;
    font-family: "Questrial", sans-serif;
    white-space: nowrap;
  }
  .brand__mark {
    border-radius: 50%;
    flex: none;
  }
  .card--front .brand {
    left: 150px;
    top: 147px;
    color: var(--card-white);
    font-size: 28px;
  }
  .card--front .brand__mark {
    width: 56px;
    height: 56px;
    background: var(--card-white);
  }
  /* Back: white contact side */
  .card--back {
    left: 510px;
    top: 465px;
    background: var(--card-white);
  }
  .card--back .brand {
    left: 28px;
    top: 44px;
    color: var(--leaf-green);
    font-size: 17px;
    gap: 10px;
  }
  .card--back .brand__mark {
    width: 34px;
    height: 34px;
    background: var(--leaf-green);
  }
  .business-name {
    position: absolute;
    left: 270px;
    top: 72px;
    font-family: "Questrial", sans-serif;
    font-size: 27px;
    letter-spacing: 0.5px;
    color: var(--ink);
    white-space: nowrap;
  }
  .contact {
    position: absolute;
    left: 300px;
    top: 150px;
    font-family: "Tinos", serif;
    font-size: 14px;
    line-height: 22px;
    color: var(--ink);
  }
  .contact__row { display: flex; gap: 10px; }
  .contact__label {
    width: 44px;
    text-align: right;
    font-weight: 700;
    color: var(--leaf-green);
  }
  .wave {
    position: absolute;
    left: 0;
    top: 0;
    width: 620px;
    height: 354px;
  }
  .tagline {
    font-family: "Questrial", sans-serif;
    font-size: 15px;
    letter-spacing: 5px;
    fill: var(--card-white);
  }
</style>
</head>
<body>
<main class="canvas">
  <section class="card card--front" aria-label="Business card front">
    <div class="brand">
      <span class="brand__mark"></span>
      <span class="brand__name">Zenova Health Massage</span>
    </div>
  </section>

  <section class="card card--back" aria-label="Business card back">
    <svg class="wave" viewBox="0 0 620 354" aria-hidden="true">
      <defs>
        <linearGradient id="waveFill" x1="0" y1="0" x2="0" y2="1">
          <stop offset="0" stop-color="var(--wave-blue)"/>
          <stop offset="1" stop-color="var(--wave-blue-deep)"/>
        </linearGradient>
        <path id="taglinePath" d="M20,232 C190,226 380,292 600,352"/>
      </defs>
      <path d="M0,182 C180,162 400,232 620,316" fill="none" stroke="var(--wave-line)" stroke-width="3"/>
      <path d="M0,196 C190,178 410,250 620,330 L620,354 L0,354 Z" fill="url(#waveFill)"/>
      <text class="tagline"><textPath href="#taglinePath">MASSAGE THERAPY AND HEALTHY FOOD</textPath></text>
    </svg>

    <div class="brand">
      <span class="brand__mark"></span>
      <span class="brand__name">Zenova Health Massage</span>
    </div>

    <h1 class="business-name">Zenova Health Massage</h1>

    <div class="contact">
      <div class="contact__row"><span class="contact__label">ph:</span><span>0413886207</span></div>
      <div class="contact__row"><span class="contact__label">email:</span><span>hello@zenovamail.com</span></div>
    </div>
  </section>
</main>
</body>
</html>
```